Looking for a unique designer to design new & exciting stationery for progressive professional firm

Hello! We would like to stand out, but in a good way. We want a modern unique image, something creative, but remain professional. Also portray integrity and look approachable. We want to appeal to the younger generation while not losing the respect of our more conservative older clients!

Our focus at Harbourline Partners is on guiding our clients and assisting them to 'Clear advice for every step'. We are a small boutique accounting firm based in Melbourne Australia.

Using our 2 distinctive colours (blue & yellow) and new logo design attached, please design a modern and professional letterhead, with compliments slip and business card for our firm.

The necessary words and logos to be included on the letterhead and card are attached, the overall design of the stationery however is up to your talent. Font to be modern, professional & progressive! I like the font style (TextPad Trebuchet MS) on my draft letterhead design attached. It looks modern, professional but approachable so something like that would be great.

For the business card, I like the attached version's REAR side of the business card but not the front side, so please come up with a design for the front that will match the letterhead design you come up with. I don't like how the company name sits tightly below the logo, they make the logo look too large in proportion to the words. Also feel free to change the rear side if you believe you have a better design :)

The colours are blue R31 G125 B165
and yellow R224 G201 B24, but please convert to CMYK equivalent.

At full sizing for the card, withcomps slip and letterhead respectively, the images need to be at least 300 dpi or higher.

Please advise if you need any other files (eg for higher resolution) or information and/or refer to our website for further input.

Thank you, with great anticipation...

Glen

Target Market(s)

Discerning (and wealthy?) clients, both business owners and personal, looking for a progressive, approachable but professional accounting firm. Need to attract and appeal to the younger generations while not losing the respect of the older more conservative generation.

Industry/Entity Type

Accounting

Font styles to use
Other font styles liked:
• Something like TextPad's Trebuchet MS - for company name. Happy for you to suggest other font for other wording.

Requirements
Must have
• My company logo, QFR logo, the wording I have included on the sample of letterhead and business card.
• The colours are blue R31 G125 B165 and yellow R224 G201 B24, but please convert to CMYK equivalent. Also use a grey for smaller wording. Refer sample letterhead attached. Note that the blue and yellow on the QFR logo are not the same as the my blue and yellow above. They will and should look different.
• Note: QFR logo must have a space around it of at least half the width of the yellow part of the logo - per my attached letter sample. The logo must be at least 15mm in width on all stationery. Also the QFR logo must have the words adjacent to it, 'Harbourline Partners Pty Ltd is a QFR practice'.
Nice to have
• Maybe curved features at bottom and/or top of letterhead instead of the rectangle coloured bars that my sample letter has.
• Good to maybe have Icons for telephone, fax email address etc.
Should not have
• No other colours except my blue, yellow and black, grey and white.
• No detailed pictures as I want to keep the design modern, minimalistic and flat.

```html
<!DOCTYPE html>
<html lang="en">
<head>
<meta charset="utf-8">
<title>Harbourline Partners Letterhead</title>
<link href="https://fonts.googleapis.com/css2?family=Lato:ital,wght@0,400;0,700;1,400&display=swap" rel="stylesheet">
<style>
  :root {
    --brand-blue: #1F7DA5;
    --brand-yellow: #E0C918;
    --tagline-gold: #A8961A;
    --ink-grey: #4A4A4A;
    --paper: #F5F4F2;
    --backdrop: #E4E4E4;
  }
  * { margin: 0; padding: 0; box-sizing: border-box; }
  html, body {
    width: 938px; height: 1200px; overflow: hidden;
    background: var(--backdrop);
    font-family: "Lato", sans-serif;
  }
  .letterhead {
    position: absolute; left: 43px; top: 0;
    width: 851px; height: 1200px;
    background: var(--paper);
    overflow: hidden;
  }
  .wave { position: absolute; left: 0; width: 851px; }
  .wave--top { top: 0; height: 100px; }
  .wave--bottom { bottom: 0; height: 70px; }

  .office-details {
    position: absolute; right: 35px; top: 8px;
    text-align: right; color: #fff; font-style: normal;
    font-size: 10.5px; line-height: 12.4px;
  }
  .office-details .abn { margin-top: 4px; }

  .brand {
    position: absolute; left: 39px; top: 31px;
    display: flex; align-items: center; gap: 14px;
  }
  .brand__dot {
    width: 48px; height: 48px; border-radius: 50%;
    background: var(--brand-yellow);
  }
  .brand__name {
    color: var(--brand-blue); font-size: 15px; letter-spacing: 0.2px;
    line-height: 16px; text-transform: uppercase;
  }
  .brand__tagline {
    color: var(--tagline-gold); font-size: 10px; margin-left: 8px; line-height: 12px;
  }

  .accreditation {
    position: absolute; left: 46px; top: 88px;
    display: flex; align-items: center; gap: 5px;
  }
  .accreditation__badge { width: 54px; height: 23px; display: flex; }
  .accreditation__badge span:first-child { flex: 2; background: #1B5FA0; }
  .accreditation__badge span:last-child { flex: 1; background: #F5D000; }
  .accreditation__text {
    color: var(--brand-blue); font-weight: 700; font-size: 8.6px; line-height: 11px;
    text-transform: uppercase;
  }

  .contact-line {
    position: absolute; left: 0; right: 0; top: 1124px;
    display: flex; justify-content: center; align-items: center; gap: 5px;
    font-size: 10px; color: var(--ink-grey);
  }
  .contact-line svg { width: 10px; height: 10px; fill: var(--brand-blue); }
  .contact-line .item { display: flex; align-items: center; gap: 3px; }
  .legal-line {
    position: absolute; left: 0; right: 0; top: 1145px;
    text-align: center; font-size: 9.4px; color: var(--ink-grey); font-style: italic;
  }
  .legal-line .principal { color: var(--brand-blue); font-style: normal; }
</style>
</head>
<body>
<main class="letterhead">
  <svg class="wave wave--top" viewBox="0 0 851 100" preserveAspectRatio="none" aria-hidden="true">
    <path d="M0,0 H851 V92 Q560,10 0,22 Z" fill="var(--brand-blue)"/>
  </svg>

  <address class="office-details">
    <div>Accountants &amp; Business Advisors</div>
    <div>Suite 408,&nbsp; 17 Bellamy Terrace</div>
    <div>Kewdale&nbsp; Victoria&nbsp; 3188</div>
    <div class="abn">ABN 12 345 678 901</div>
  </address>

  <header class="brand">
    <div class="brand__dot"></div>
    <div>
      <div class="brand__name">Harbourline Partners</div>
      <div class="brand__tagline">Clear advice for every step</div>
    </div>
  </header>

  <div class="accreditation">
    <div class="accreditation__badge"><span></span><span></span></div>
    <div class="accreditation__text">Harbourline Partners Pty Ltd<br>is a QFR practice</div>
  </div>

  <footer>
    <div class="contact-line">
      <span class="item">
        <svg viewBox="0 0 24 24"><path d="M6.6 10.8a15.1 15.1 0 0 0 6.6 6.6l2.2-2.2c.3-.3.7-.4 1-.2 1.1.4 2.3.6 3.6.6.6 0 1 .4 1 1V20c0 .6-.4 1-1 1A17 17 0 0 1 3 4c0-.6.4-1 1-1h3.5c.6 0 1 .4 1 1 0 1.3.2 2.5.6 3.6.1.3 0 .7-.2 1z"/></svg>
        +61 3 9000 1234
      </span>
      <span class="item">
        <svg viewBox="0 0 24 24"><path d="M6 3h10v5H6zM3 9h18v9h-3v3H6v-3H3zm5 6v4h8v-4z"/></svg>
        +61 3 9000 1235
      </span>
      <span class="item">
        <svg viewBox="0 0 24 24"><path d="M2 5h20v14H2zm2 2v.5l8 5 8-5V7l-8 5z"/></svg>
        hello@harbourlinepartners.example
      </span>
      <span class="item">
        <svg viewBox="0 0 24 24"><path d="M12 2a10 10 0 1 0 0 20 10 10 0 0 0 0-20zm-1 17.9A8 8 0 0 1 4.2 10L9 15v1a2 2 0 0 0 2 2zm6.9-2.5A2 2 0 0 0 16 16h-1v-3a1 1 0 0 0-1-1H8v-2h2a1 1 0 0 0 1-1V7h2a2 2 0 0 0 2-2v-.4a8 8 0 0 1 2.9 12.8z"/></svg>
        harbourlinepartners.example
      </span>
    </div>
    <p class="legal-line">Liability limited by a scheme approved under Professional Standards Legislation - <span class="principal">Glen A Hartley&nbsp; BBus, QFR, RTA</span></p>
  </footer>

  <svg class="wave wave--bottom" viewBox="0 0 851 70" preserveAspectRatio="none" aria-hidden="true">
    <path d="M0,11 Q380,66 851,65 V70 H0 Z" fill="var(--brand-yellow)"/>
  </svg>
</main>
</body>
</html>
```